Brook Forge - Crypto Currency Miner Powered by Renewable Energy Website

We Need Web Pages Design for Website for Crypto Currency Miner

Serivices include:
Mining Rig Sales
Housing for Rigs turnkey on renewable energy grid
Cloud Mining term packages
Updates

http://www.vaultrigratings.example (Competitors sites)

Target Market(s)

Investers for Mining Rigs and terms for 1,2 or 3 years of Hash rate

Industry/Entity Type

Mining

Number of Pages Required

5+ page

Font styles to use
Sans Serif

Colors
add136
9bcb3c
606060
474747
ffc214
cadf82
fbee3e
876aae
6b449b

Requirements
Must have
• Pictures of Solar, Wind and power Factor Correction units
Nice to have
• e-commerce platform so contract terms can be purchased through website
Should not have
• Heavy construction equipment

```html
<!DOCTYPE html>
<html lang="en">
<head>
<meta charset="utf-8">
<title>Brook Forge – Crypto Mining on Renewable Energy</title>
<link rel="stylesheet" href="https://fonts.googleapis.com/css2?family=Ropa+Sans&family=Open+Sans:wght@400;600&display=swap">
<style>
:root{
  --green:#9bcb3c;
  --green-bright:#add136;
  --blue:#0a8bcc;
  --ink:#474747;
  --grey:#606060;
  --line:#dcdcdc;
  --field:#f4f4f4;
  --white:#ffffff;
}
*{box-sizing:border-box;margin:0;padding:0}
html,body{width:1200px;height:2961px;overflow:hidden}
body{position:relative;font-family:"Open Sans",Arial,sans-serif;color:var(--ink);background:var(--white)}
.abs{position:absolute}
.head{font-family:"Ropa Sans","Arial Narrow",sans-serif;font-weight:400}

/* hero */
.hero{left:0;top:0;width:1200px;height:586px;background:linear-gradient(160deg,#e9f6ff 0%,#9fd2f3 30%,#3f9ee0 70%,#2d86cf 100%)}
.hero-panel{left:572px;top:130px;width:528px;height:456px;background:linear-gradient(135deg,#3a5aa8 0%,#1f3f86 60%,#6e8fbf 100%);opacity:.85;border-radius:4px}
.brand{left:84px;top:22px;display:flex;align-items:center;gap:10px}
.brand-dot{width:46px;height:46px;border-radius:50%;background:var(--green)}
.brand-name{font-family:"Ropa Sans",sans-serif;font-size:28px;color:var(--ink)}
.nav{left:0;top:56px;width:1200px;height:20px;font-family:"Ropa Sans",sans-serif;font-size:14px;color:var(--white);letter-spacing:.3px}
.nav span{position:absolute;top:0}
.nav-mark{left:452px;top:100px;width:124px;height:3px;background:var(--green)}
.hero-title{left:80px;top:244px;font-size:64px;letter-spacing:2px;color:#3b3b3b;line-height:1}
.hero-sub{left:80px;top:322px;font-size:32px;letter-spacing:1.5px;color:#3b3b3b;line-height:1}
.zip{display:flex;border:4px solid rgba(255,255,255,.85);background:var(--white)}
.zip-field{flex:1;font-family:"Ropa Sans",sans-serif;display:flex;align-items:center;padding-left:20px;color:#666;white-space:nowrap}
.zip-btn{background:var(--green);color:var(--white);font-family:"Ropa Sans",sans-serif;display:flex;align-items:center;justify-content:center;letter-spacing:.5px;white-space:nowrap}
.hero-zip{left:83px;top:400px;width:388px;height:46px}
.hero-zip .zip-field{font-size:15px;color:#333}
.hero-zip .zip-btn{width:210px;font-size:15px}

/* section headings */
.squiggle{display:block}
.sec-title{font-size:34px;line-height:1}
.sec-sub{font-size:20px;line-height:1;letter-spacing:.5px}

/* about */
.about-title{left:79px;top:635px;color:#333}
.about-sub{left:79px;top:675px;color:var(--grey)}
.about-sq{left:79px;top:708px}
.about-copy{left:79px;top:742px;width:640px;font-size:12.5px;line-height:21px;color:#444}
.about-copy p+p{margin-top:21px}
.about-art{left:730px;top:620px;width:405px;height:390px;background:radial-gradient(ellipse at 55% 45%,#7cc04a 0%,#b9dca0 40%,#ffffff 72%)}

/* services */
.solutions{left:0;top:1010px;width:1200px;height:504px;background:var(--blue);color:var(--white);text-align:center}
.solutions .sec-title{position:absolute;top:38px;width:100%}
.solutions .sec-sub{position:absolute;top:78px;width:100%;font-size:21px}
.solutions .squiggle{position:absolute;top:112px;left:530px}
.sol-card{top:170px;width:300px}
.sol-icon{display:block;margin:0 auto;height:90px}
.sol-name{font-family:"Ropa Sans",sans-serif;font-size:21px;letter-spacing:.6px;margin-top:28px}
.sol-text{font-size:12.5px;line-height:20px;margin:14px auto 0;width:270px}
.sol-btn{display:inline-block;margin-top:24px;width:108px;height:34px;line-height:32px;border:1.5px solid var(--white);font-size:12px;font-weight:600}

/* updates */
.upd-title{left:0;top:1554px;width:1200px;text-align:center;color:#333}
.upd-sub{left:0;top:1594px;width:1200px;text-align:center;color:var(--grey)}
.upd-sq{left:530px;top:1624px}
.card{top:1678px;width:310px;height:424px;border:1px solid var(--line);background:var(--white);text-align:center}
.card-photo{width:100%;height:247px}
.card-body{height:175px;padding-top:38px}
.card-name{font-family:"Ropa Sans",sans-serif;font-size:17px;color:#333;letter-spacing:.3px}
.card-rule{width:36px;height:2px;background:var(--green);margin:10px auto 18px}
.card-text{font-size:12px;line-height:22px;color:#555;width:260px;margin:0 auto}

/* lock band */
.lock{left:0;top:2166px;width:1200px;height:100px;background:var(--blue);color:var(--white)}
.lock-title{left:94px;top:16px;font-size:34px;line-height:1}
.lock-sub{left:94px;top:58px;font-size:13px;font-weight:600}
.lock-zip{left:604px;top:21px;width:472px;height:62px;border-width:6px;border-color:#d6ecf8}
.lock-zip .zip-field{font-size:15px;color:#9a9a9a}
.lock-zip .zip-btn{width:226px;font-size:16px}

/* footer */
.footer{left:0;top:2266px;width:1200px;height:375px;background:var(--green);color:var(--white)}
.f-head{font-family:"Ropa Sans",sans-serif;font-size:21px;letter-spacing:.5px;top:30px}
.f-text{font-size:13px;line-height:19px}
.f-list{list-style:none;font-size:14px;line-height:25px}
.f-list li::before{content:"";display:inline-block;border-left:6px solid var(--white);border-top:4px solid transparent;border-bottom:4px solid transparent;margin-right:9px}
.news-field{left:594px;top:117px;width:237px;height:34px;background:var(--white);color:#999;font-size:12px;padding:9px 10px}
.news-btn{left:748px;top:160px;width:83px;height:32px;background:var(--ink);color:var(--white);font-size:12px;border-radius:3px;text-align:center;line-height:32px}
.contact-row{display:flex;gap:12px;font-size:14px;line-height:19px}

.base{left:0;top:2641px;width:1200px;height:320px;background:#484848}
.hello{left:79px;top:2503px;width:1038px;height:379px;background:var(--white)}
.hello-title{left:0;top:34px;width:100%;text-align:center;font-size:32px;letter-spacing:1px;color:#333}
.field{background:var(--field);border:1px solid #e6e6e6;font-size:11px;color:#777;padding:10px 16px}
.submit{left:430px;top:288px;width:154px;height:46px;background:var(--blue);color:var(--white);font-size:14px;letter-spacing:1px;text-align:center;line-height:46px;border-radius:3px;font-weight:600}
.copy{left:80px;top:2911px;font-size:14px;color:var(--white);letter-spacing:.4px}
.social{left:953px;top:2904px;display:flex;gap:10px}
.social span{width:28px;height:28px;border-radius:50%;border:2px solid var(--white)}
</style>
</head>
<body>

<header class="abs hero" role="img" aria-label="Bright blue sky with sunlight and clouds"></header>
<div class="abs hero-panel" role="img" aria-label="Solar panel that powers the mining farm, mounted on a pole against the sky"></div>

<div class="abs brand"><span class="brand-dot"></span><span class="brand-name">Brook Forge</span></div>

<nav class="abs nav">
  <span style="left:456px">MINING RIGS</span>
  <span style="left:606px">RIG HOUSING</span>
  <span style="left:762px">CLOUD MINING</span>
  <span style="left:906px">UPDATES</span>
  <span style="left:1052px">COMPANY</span>
</nav>
<div class="abs nav-mark"></div>

<h1 class="abs head hero-title">CRYPTO MINING</h1>
<p class="abs head hero-sub">POWERED BY THE SUN</p>
<div class="abs zip hero-zip"><div class="zip-field">HASH RATE</div><div class="zip-btn">CALCULATE YOUR EARNINGS</div></div>

<!-- about -->
<h2 class="abs head sec-title about-title">About Us</h2>
<p class="abs head sec-sub about-sub">Mining Expertise. Delivered.</p>
<svg class="abs squiggle about-sq" width="84" height="14" viewBox="0 0 84 14"><path d="M0 7H34L37 3 40 11 43 2 46 9 49 7H84" fill="none" stroke="#0a8bcc" stroke-width="1.5"/></svg>
<div class="abs about-copy">
  <p>Brook Forge is a crypto currency mining company based in Rivermoor Eastvale that runs its mining farm entirely on renewable energy. Our solar fields, wind turbines and power factor correction units keep every rig running clean, cool and at low cost. Our team of engineers has a combined experience of over 50 years in power and computing, with a 100% uptime record across our hosted rigs.</p>
  <p>We sell proven mining rigs, house them turnkey on our renewable energy grid, and offer cloud mining terms for investors who prefer to buy hash rate without owning hardware. Every rig is monitored around the clock, and investors can follow output, power use and payouts from one account.</p>
</div>
<div class="abs about-art" role="img" aria-label="Hand holding a tablet with a tree and wind turbines on green grass"></div>

<!-- services -->
<section class="abs solutions">
  <h2 class="head sec-title">Mining Services</h2>
  <p class="head sec-sub">Rig Sales, Rig Housing, and Cloud Mining</p>
  <svg class="squiggle" width="140" height="14" viewBox="0 0 140 14"><path d="M0 7H60L63 3 66 11 69 2 72 9 75 7H140" fill="none" stroke="#fff" stroke-width="1.5"/></svg>

  <div class="abs sol-card" style="left:83px">
    <svg class="sol-icon" width="80" height="90" viewBox="0 0 80 90"><circle cx="40" cy="22" r="18" fill="#fff"/><text x="40" y="30" font-size="22" font-family="Arial" font-weight="700" text-anchor="middle" fill="#0a8bcc">$</text><path d="M6 40V66L24 86H34V68L20 54M74 40V66L56 86H46V68L60 54" fill="none" stroke="#fff" stroke-width="7" stroke-linejoin="round"/></svg>
    <div class="sol-name">BUY MINING RIGS</div>
    <p class="sol-text">Choose from tested, ready to run mining rigs. Each unit ships configured, so your rig starts earning from the day it is switched on.</p>
    <span class="sol-btn">Read More</span>
  </div>
  <div class="abs sol-card" style="left:444px">
    <svg class="sol-icon" width="80" height="90" viewBox="0 0 80 90"><path d="M40 4 76 38H66V86H14V38H4Z" fill="#fff"/><rect x="56" y="8" width="8" height="18" fill="#fff"/><text x="40" y="74" font-size="36" font-family="Arial" font-weight="700" text-anchor="middle" fill="#0a8bcc">$</text></svg>
    <div class="sol-name">HOUSE YOUR RIGS</div>
    <p class="sol-text">We host your rigs turnkey on our renewable energy grid, with cooling, security and round the clock monitoring included.</p>
    <span class="sol-btn">Read More</span>
  </div>
  <div class="abs sol-card" style="left:794px">
    <svg class="sol-icon" width="80" height="90" viewBox="0 0 80 90"><circle cx="40" cy="16" r="7" fill="#fff"/><path d="M28 10 23 6M52 10 57 6M40 4V0" stroke="#fff" stroke-width="2"/><rect x="10" y="30" width="60" height="44" rx="3" fill="none" stroke="#fff" stroke-width="4"/><path d="M10 44H70M10 59H70M25 30V74M40 30V74M55 30V74" stroke="#fff" stroke-width="3"/><path d="M36 74V86M24 86H56" stroke="#fff" stroke-width="4"/></svg>
    <div class="sol-name">CLOUD MINING TERMS</div>
    <p class="sol-text">Buy hash rate for 1, 2 or 3 years at a fixed price. No hardware to manage, with payouts sent straight to your wallet.</p>
    <span class="sol-btn">Read More</span>
  </div>
</section>

<!-- updates -->
<h2 class="abs head sec-title upd-title">Stay Up To Date</h2>
<p class="abs head sec-sub upd-sub">News From Our Mining Farm.</p>
<svg class="abs squiggle upd-sq" width="140" height="14" viewBox="0 0 140 14"><path d="M0 7H60L63 3 66 11 69 2 72 9 75 7H140" fill="none" stroke="#0a8bcc" stroke-width="1.5"/></svg>

<article class="abs card" style="left:103px">
  <div class="card-photo" role="img" aria-label="Rows of solar panels in a field" style="background:linear-gradient(135deg,#c9d9ee,#4d6fa8,#a9bfdc)"></div>
  <div class="card-body"><div class="card-name">SOLAR FIELD EXPANSION</div><div class="card-rule"></div><p class="card-text">New panels now power a second hall of hosted rigs.</p></div>
</article>
<article class="abs card" style="left:440px">
  <div class="card-body"><div class="card-name">WIND POWER ONLINE</div><div class="card-rule"></div><p class="card-text">Our turbines keep the farm running through the night.</p></div>
  <div class="card-photo" role="img" aria-label="Wind turbines on a green hill under a blue sky" style="height:249px;background:linear-gradient(160deg,#cfe6f6,#8cc3e6,#6c9a3c)"></div>
</article>
<article class="abs card" style="left:778px">
  <div class="card-photo" role="img" aria-label="Power factor correction units in an electrical room" style="background:linear-gradient(160deg,#d8dde2,#8e9aa4,#56626c)"></div>
  <div class="card-body"><div class="card-name">POWER FACTOR CORRECTION</div><div class="card-rule"></div><p class="card-text">New units cut grid losses and lower cost per hash.</p></div>
</article>

<!-- lock band -->
<section class="abs lock">
  <h2 class="abs head lock-title">Lock in Your Hash Rate</h2>
  <p class="abs lock-sub">No price hikes. Buy a 1, 2 or 3 year cloud mining term today.</p>
  <div class="abs zip lock-zip"><div class="zip-field">HASH RATE</div><div class="zip-btn">CALCULATE YOUR EARNINGS</div></div>
</section>

<!-- footer -->
<footer class="abs footer">
  <h3 class="abs f-head" style="left:85px">ABOUT US</h3>
  <div class="abs f-text" style="left:85px;top:68px;width:250px">
    <p>Brook Forge offers crypto mining on a fully renewable grid, with services like</p>
    <p style="margin-top:19px">Mining Rig Sales<br>Rig Housing and Cloud Mining Terms.</p>
  </div>
  <h3 class="abs f-head" style="left:413px;top:34px">COMPANY</h3>
  <ul class="abs f-list" style="left:410px;top:69px">
    <li>About Us</li><li>Mining Rigs</li><li>Rig Housing</li><li>Cloud Mining</li><li>Contact Us</li>
  </ul>
  <h3 class="abs f-head" style="left:598px;top:32px">NEWSLETTER</h3>
  <p class="abs f-text" style="left:598px;top:66px;width:240px">Get farm news and new mining terms by email.</p>
  <div class="abs news-field">Enter Your Email</div>
  <div class="abs news-btn">Subscribe</div>
  <h3 class="abs f-head" style="left:918px">CONTACT US</h3>
  <div class="abs contact-row" style="left:914px;top:68px">
    <svg width="16" height="18" viewBox="0 0 16 18"><path d="M4 1C2 1 1 3 1 5 1 11 6 17 12 17 14 17 15 15 15 14L12 11 10 13C7 12 5 10 4 7L6 5Z" fill="#fff"/></svg>
    <span>(0150) 555 0142</span>
  </div>
  <div class="abs contact-row" style="left:914px;top:104px">
    <svg width="16" height="20" viewBox="0 0 16 20"><path d="M8 0C4 0 1 3 1 7 1 12 8 20 8 20S15 12 15 7C15 3 12 0 8 0Z" fill="#fff"/><circle cx="8" cy="7" r="2.6" fill="#9bcb3c"/></svg>
    <span>Brook Forge<br>48 Meadow Park,<br>Sector II, Rivermoor,<br>Eastvale – 560419</span>
  </div>
</footer>

<div class="abs base"></div>

<section class="abs hello">
  <h2 class="abs head hello-title">SAY HELLO</h2>
  <div class="abs field" style="left:59px;top:103px;width:445px;height:36px">Full Name</div>
  <div class="abs field" style="left:59px;top:162px;width:445px;height:36px">Email Address</div>
  <div class="abs field" style="left:59px;top:217px;width:445px;height:36px">Phone Number</div>
  <div class="abs field" style="left:535px;top:103px;width:446px;height:148px">Your Message</div>
  <div class="abs submit">SUBMIT</div>
</section>

<p class="abs copy">All rights reserved. © 2015-2016 Brook Forge</p>
<div class="abs social"><span></span><span></span><span></span><span></span><span></span></div>

</body>
</html>
```